Lakeshore Freightways Council Web Update

Update wordpress based association web site. Please look up www.lakeshorefreightwayscouncil.com for our web site to get a feel for what we currently having. We would like our updated web site to look similar to: www.brightoakfund.com. We will provide our key points for updating in a future email.

Target Market(s)

duplicate the brightoakfund.com format please.

Number of Pages Required

4 page

Font styles to use
Serif

Requirements
Must have
• duplicate the brightoakfund.com format please. You will keep most of the content that we currently have on our website.
Nice to have
• n/a
Should not have
• n/a

```html
<!DOCTYPE html>
<html lang="en">
<head>
<meta charset="utf-8">
<title>Lakeshore Freightways Council</title>
<link href="https://fonts.googleapis.com/css2?family=Arimo:wght@400;700&family=Libre+Baskerville:wght@700&display=swap" rel="stylesheet">
<style>
:root{
  --navy:#1f1f6e;
  --navy-panel:rgba(30,30,115,.94);
  --navy-deep:#181857;
  --heading:#1c2d8c;
  --white:#ffffff;
  --ink:#333;
  --top:#f2f2f2;
}
*{box-sizing:border-box;margin:0;padding:0}
html,body{width:1200px;height:4145px;overflow:hidden;background:var(--white);font-family:"Arimo",Arial,sans-serif;color:var(--ink)}
body{position:relative}
.topbar{height:25px;background:var(--top);display:flex;align-items:center;justify-content:space-between;padding:0 22px;font-size:10px;color:#555}
.topbar .info{display:flex;gap:20px}
.topbar .social{display:flex;gap:6px}
.dot{width:12px;height:12px;border-radius:50%;background:var(--navy)}
.header{height:53px;display:flex;align-items:center;justify-content:space-between;padding:0 22px}
.brand{display:flex;align-items:center;gap:10px;font-family:"Libre Baskerville",Georgia,serif;font-weight:700;color:var(--navy);font-size:17px}
.brand-square{width:30px;height:30px;background:var(--navy)}
.header .actions{display:flex;gap:8px}
.btn-menu{border:1px solid #999;color:#555;font-size:11px;padding:5px 10px}
.btn-login{background:var(--navy);color:#fff;font-size:11px;padding:6px 12px}
.hero{position:relative;height:586px;background:linear-gradient(180deg,#2c3a63 0%,#5d6688 45%,#8a6b74 70%,#2a2a30 100%)}
.hero h1{position:absolute;left:152px;top:165px;width:450px;color:#fff;font-size:20px;line-height:1.3;font-weight:700}
.hero .chev{position:absolute;left:586px;bottom:18px}
.hero .dots{position:absolute;right:60px;bottom:26px;display:flex;gap:6px}
.hero .dots span{width:9px;height:9px;border-radius:50%;background:#fff;opacity:.6}
.hero .dots span:first-child{opacity:1;background:#4aa0ff}
.section-title{position:absolute;left:0;width:1200px;text-align:center;color:var(--heading);font-size:26px;font-weight:700;line-height:1}
.band{position:absolute;left:0;width:1200px}
.photo{position:absolute;inset:0}
.panel{position:absolute;top:0;bottom:0;width:428px;background:var(--navy-panel);color:#fff;padding:46px 38px;font-size:14.5px;line-height:1.75;letter-spacing:.2px}
.panel.right{left:600px}
.panel.left{left:172px}
.panel-photo{margin-top:22px;width:330px;height:180px}
.sig{display:flex;justify-content:flex-end;align-items:center;gap:12px;margin-top:14px;font-weight:700;text-align:right;line-height:1.3}
.avatar{width:52px;height:52px;border-radius:50%;background:#c4c8d4}
.outline-btn{display:inline-block;margin-top:30px;border:2px solid #fff;padding:10px 22px;color:#fff;font-size:14px;border-radius:3px}
.link-red{color:#ff5a5a;font-weight:700}
.form input{display:block;width:340px;height:40px;margin-top:14px;border:none;padding:0 12px;font-family:inherit;font-size:14px;color:#888}
.contact{position:absolute;top:3904px;left:0;width:1200px;height:177px;background:var(--navy);display:flex;align-items:center;padding:0 78px;color:#fff}
.contact .btns{display:flex;flex-direction:column;gap:16px;width:240px;flex-shrink:0}
.contact .btns span{border:2px solid #fff;text-align:center;padding:10px 0;font-size:13px;border-radius:3px}
.contact .items{display:flex;gap:36px;margin-left:60px;align-items:flex-start}
.item{text-align:center;font-size:13px;font-weight:700;line-height:1.4;white-space:nowrap}
.item svg{display:block;margin:0 auto 8px}
.copyright{position:absolute;top:4100px;left:0;width:1200px;height:45px;background:var(--navy-deep);color:#fff;font-size:13px;display:flex;align-items:center;justify-content:space-between;padding:0 78px}
.copyright .social{display:flex;gap:10px}
.copyright .social .dot{background:#fff;width:14px;height:14px}
</style>
</head>
<body>
<div class="topbar">
  <div class="info"><span>450 Harbor Street, Suite 210 Portvale, MI 48000</span><span>(555) 014-2200</span><span>(555) 014-2281</span><span>info@lakeshorefreightwayscouncil.com</span></div>
  <div class="social"><span class="dot"></span><span class="dot"></span><span class="dot"></span><span class="dot"></span><span class="dot"></span></div>
</div>
<header class="header">
  <div class="brand"><span class="brand-square"></span>Lakeshore Freightways Council</div>
  <div class="actions"><span class="btn-menu">Menu ☰</span><span class="btn-login">Login</span></div>
</header>

<section class="hero" role="img" aria-label="Freight locomotive with headlights on at dusk on a curving track">
  <h1>Every year America's freight railroads spend more than $20 billion annually of their own funds, not taxpayer money, to build and maintain a rail network that is safe, reliable, efficient and affordable.</h1>
  <div class="dots"><span></span><span></span><span></span><span></span></div>
  <svg class="chev" width="28" height="14" viewBox="0 0 28 14"><path d="M2 2l12 10 12-10" fill="none" stroke="#fff" stroke-width="2.5"/></svg>
</section>

<h2 class="section-title" style="top:702px">Welcome to LFC</h2>
<section class="band" style="top:763px;height:478px">
  <div class="photo" role="img" aria-label="Blue and white locomotive at night" style="background:linear-gradient(90deg,#0e1320 0%,#24407e 40%,#1a2a55 70%,#0f1424 100%)"></div>
  <div class="panel right">
    I would like to welcome you to the Lakeshore Freightways Council website. Here you will find valuable information on Michigan railroads, including issues and concerns in and around the railroad industry. We are an active and aggressive state railroad association and we look forward to continued success with our partnerships. Please make sure to click on our member railroad company links while you're here. Also, sign up for our newsletter and follow the LFC on social media. Thank you and I hope you enjoy your visit to our website.
    <div class="sig"><span>Dana Whitlock<br>President</span><span class="avatar" role="img" aria-label="Portrait of the president"></span></div>
  </div>
</section>

<h2 class="section-title" style="top:1285px">What We DO</h2>
<section class="band" style="top:1352px;height:487px">
  <div class="photo" role="img" aria-label="Orange and black locomotive approaching through green trees" style="background:linear-gradient(90deg,#3d5a2c 0%,#5e7a3e 40%,#7a5a2e 65%,#4b6a33 100%)"></div>
  <div class="panel left">
    The LFC reviews all introduced legislation in the House and Senate. Proposed legislation affecting the rail industry is shared with our members. Final industry positions regarding legislation are then communicated to the legislature. We pursue the same activity with appropriate personnel in the state departments and the legislative rules process.
    <div class="panel-photo" role="img" aria-label="Red freight locomotives on a rural line" style="background:linear-gradient(180deg,#9fb5d0,#8d7a5a)"></div>
  </div>
</section>

<h2 class="section-title" style="top:1970px">Who We Are</h2>
<section class="band" style="top:2027px;height:567px">
  <div class="photo" role="img" aria-label="Red locomotive plowing through snow" style="background:linear-gradient(90deg,#5f7f9e 0%,#8a3a2e 25%,#a9bccc 50%,#6d8aa6 100%)"></div>
  <div class="panel right">
    The Lakeshore Freightways Council (LFC) is a non-profit trade association that represents the interests of freight railroads operating in Michigan. LFC members range in size from large Class 1 interstate carriers to smaller regional carriers and shortline railroads. LFC members account for over 95% of all freight rail moved in Michigan.
    <div class="panel-photo" role="img" aria-label="Video still of a freight train among trees" style="background:linear-gradient(180deg,#6f8f4c,#3f5530);display:flex;align-items:center;justify-content:center">
      <svg width="44" height="32" viewBox="0 0 44 32"><rect width="44" height="32" rx="7" fill="#fff"/><path d="M17 9l12 7-12 7z" fill="#222"/></svg>
    </div>
  </div>
</section>

<h2 class="section-title" style="top:2650px">How to Join LFC</h2>
<section class="band" style="top:2710px;height:580px">
  <div class="photo" role="img" aria-label="Freight train curving along a lakeshore with trees" style="background:linear-gradient(90deg,#4a6a30 0%,#6a8a45 35%,#8fa8c0 60%,#4f6d35 100%)"></div>
  <div class="panel left">
    LFC membership is open to any freight railroad with Michigan operations. Please contact the LFC office for membership information. Companies which supply goods or services to the railroad industry are eligible for a non-voting Associate Membership. Annual dues are $1,000 per year for supplier members.<br><br>
    Please click <span class="link-red">HERE</span> to download the LFC Associate Membership application. Return a completed form to info@lakeshorefreightwayscouncil.com or mail to our mailing address.
    <div><span class="outline-btn">Meet our Members</span></div>
  </div>
</section>

<h2 class="section-title" style="top:3325px">Newsletter</h2>
<section class="band" style="top:3382px;height:434px">
  <div class="photo" role="img" aria-label="Locomotive with headlights at dusk" style="background:linear-gradient(90deg,#2a2e3a 0%,#3d4660 40%,#7a6a88 70%,#3a3040 100%)"></div>
  <div class="panel right" style="padding-top:60px">
    Subscribe to our Newsletter and receive latest updates.
    <div class="form"><input value="Name*" aria-label="Name"><input value="Email*" aria-label="Email"></div>
    <span class="outline-btn" style="margin-top:46px">Subscribe</span>
  </div>
</section>

<h2 class="section-title" style="top:3851px">Contact Us</h2>
<footer class="contact">
  <div class="btns"><span>RESOURCES</span><span>RAILROADS &amp; VETERANS</span></div>
  <div class="items">
    <div class="item"><svg width="22" height="28" viewBox="0 0 22 28"><path d="M11 26S3 16 3 10a8 8 0 0116 0c0 6-8 16-8 16z" fill="none" stroke="#fff" stroke-width="2"/><circle cx="11" cy="10" r="3" fill="none" stroke="#fff" stroke-width="2"/></svg>450 Harbor Street,<br>Suite 210 Portvale, MI 48000</div>
    <div class="item"><svg width="24" height="24" viewBox="0 0 24 24"><path d="M5 3l4 1 1 5-2 2a12 12 0 005 5l2-2 5 1 1 4-3 2C10 21 3 14 3 6z" fill="none" stroke="#fff" stroke-width="1.8"/></svg>(555) 014-2200</div>
    <div class="item"><svg width="26" height="24" viewBox="0 0 26 24"><rect x="7" y="2" width="12" height="7" fill="none" stroke="#fff" stroke-width="1.8"/><rect x="2" y="9" width="22" height="9" fill="none" stroke="#fff" stroke-width="1.8"/><rect x="7" y="15" width="12" height="7" fill="none" stroke="#fff" stroke-width="1.8"/></svg>(555) 014-2281</div>
    <div class="item"><svg width="28" height="22" viewBox="0 0 28 22"><rect x="2" y="2" width="24" height="18" fill="none" stroke="#fff" stroke-width="1.8"/><path d="M2 2l12 10 12-10" fill="none" stroke="#fff" stroke-width="1.8"/></svg>info@lakeshorefreightwayscouncil.com</div>
  </div>
</footer>
<div class="copyright"><span>© Copyright 2017. LFC. All rights reserved.</span><div class="social"><span class="dot"></span><span class="dot"></span><span class="dot"></span><span class="dot"></span><span class="dot"></span></div></div>
</body>
</html>
```